Website Wordpress Responsive Design and Development - Landscape Company

Site is currently under construction, but the old site needs a refresh.
Need a fully responsive wordpress website (built in Elementor or comparable theme).
Here's the way it looked prior :
https://pastpages.example/snap/20220330041341/http://brookmoorgreens.example/
Their current designer came up with a website sample and it looks terrible :
https://talkowenpics.sitebuild.example/mysite/projects
Websites the client likes for some inspiration, but needs better than these :
https://www.quarrinbeckgroundworkers.example/
http://kvatelierpx.example/
https://tullidgepartners.example/
https://www.garbettcoinc.example/

Navigation includes :
• Home
• Complete structure of website content is available in the home page, yielding main information on services.
• Visually appealing but simple to use and navigate. Subtle amount of content, but enough for search engines to be able to read up the target phrases.
• Sections on the home page include :
▪ About - Information about the company and main service focus
▪ Gallery - Imagery categorized to include lightbox style zoom.
▪ Contact - Contact details and connection information
• About
• Bannered header
• Content appropriately formatted to subject
• Gallery
• Bannered header
• Each of the albums would have their own categorized image content
• Contact
• Bannered header
• Social Media connector available on all pages (like box, feed, etc) if applicable
• Content can be updated on all pages
• Basic Optimization for SEO with title tags, meta data where applicable.
• Google Analytics and Sitemap installed. (google account will be provided)
• Google Business Listing and Search Console Accounts created

Coded - Design and coding required

1 page

• Wordpress Responsive Design

```html
<!DOCTYPE html>
<html lang="en">
<head>
<meta charset="utf-8">
<title>Brookmoor Greens – Outdoor Living</title>
<link rel="stylesheet" href="https://fonts.googleapis.com/css2?family=Montserrat:wght@400;500;600;700&display=swap">
<style>
:root{
  --green:#55c157;
  --green-dark:#3fa742;
  --ink:#1f1f1f;
  --text:#2b2b2b;
  --grey-panel:#8c8c8c;
  --footer:#332d2d;
  --white:#ffffff;
}
*{box-sizing:border-box;margin:0;padding:0}
html,body{width:1200px;height:4141px;overflow:hidden;background:var(--white)}
body{position:relative;font-family:'Montserrat',sans-serif;color:var(--text)}
.abs{position:absolute}
.social{display:flex;gap:8px}
.social span{width:21px;height:21px;background:var(--green);border-radius:2px;display:block}
.brand{left:0;width:1200px;top:48px;text-align:center}
.brand small{display:block;font-size:12px;font-weight:600;color:var(--ink)}
.brand strong{display:block;font-size:25px;font-weight:600;color:var(--ink);margin-top:2px}
.phone{left:920px;top:48px;width:121px;text-align:center;font-size:13px;font-weight:600;color:var(--ink)}
.btn{display:inline-block;background:var(--green);color:var(--white);font-size:9px;font-weight:600;letter-spacing:.3px;padding:7px 11px;border-radius:3px;text-transform:uppercase}
.btn-top{left:919px;top:72px;width:122px;text-align:center;font-size:10px}
.nav{left:0;top:129px;width:1200px;height:64px;background:var(--green)}
.nav ul{list-style:none;display:flex;justify-content:center;gap:0;height:100%;align-items:center}
.nav li{font-size:12px;font-weight:500;color:var(--white);text-transform:uppercase;padding:0 28px}
.hero{left:0;top:193px;width:1200px;height:550px;background:linear-gradient(180deg,#4f6a45 0%,#5f8a3e 40%,#7fa653 70%,#3c5a2a 100%)}
.hero h1{position:absolute;left:0;width:1200px;top:170px;text-align:center;color:var(--white);font-size:41px;font-weight:500;line-height:49px;text-transform:uppercase}
.hero p{position:absolute;left:0;width:1200px;top:290px;text-align:center;color:var(--white);font-size:19px;font-weight:500;text-transform:uppercase}
.heading{display:flex;align-items:center;gap:16px;color:var(--green);font-size:23px;font-weight:700;text-transform:uppercase}
.heading::before,.heading::after{content:"";width:52px;height:3px;background:var(--green)}
.body-copy{font-size:14.5px;line-height:25px;color:var(--text)}
.photo{display:block}
.contact-panel{background:var(--grey-panel);color:var(--white)}
.contact-panel h3{font-size:22px;font-weight:500;margin-bottom:22px}
.contact-panel p{font-size:14px;line-height:25px;color:#eeeeee}
.service h2{font-size:23px;font-weight:500;color:var(--ink)}
.service h2::after{content:"";display:block;width:75px;height:2px;background:var(--green);margin-top:10px}
.service p{margin-top:18px;margin-bottom:24px}
.contact-us{color:var(--white)}
.contact-us h2{font-size:23px;font-weight:600;text-transform:uppercase;margin-bottom:20px}
.contact-us p{font-size:14px;line-height:25px}
.field{background:var(--white);font-size:11px;color:#9a9a9a;padding:12px 17px}
.send{background:#eef7ee;color:var(--green);font-size:9px;font-weight:700;text-align:center;padding:7px 0;border-radius:3px}
.footer{left:0;top:3972px;width:1200px;height:169px;background:var(--footer);color:var(--white)}
.footer .social{position:absolute;left:530px;top:34px;gap:9px}
.footer .social span{background:var(--white)}
.footer ul{position:absolute;top:80px;left:0;width:1200px;list-style:none;display:flex;justify-content:center}
.footer li{font-size:12px;font-weight:500;text-transform:uppercase;padding:0 27px}
.footer .copy{position:absolute;top:127px;width:1200px;text-align:center;font-size:9px}
</style>
</head>
<body>

<header>
  <div class="abs social" style="left:161px;top:62px"><span></span><span></span><span></span><span></span><span></span></div>
  <div class="abs brand"><small>Logo</small><strong>brookmoorgreens</strong></div>
  <div class="abs phone">555-014-2290</div>
  <div class="abs btn btn-top">Request Estimate</div>
</header>

<nav class="abs nav"><ul>
  <li>Home</li><li>About Us</li><li>Services &#8964;</li><li>Portfolio</li><li>Gallery</li><li>Contact</li>
</ul></nav>

<section class="abs hero" role="img" aria-label="Photo of a landscaped garden path with shrubs, lawn and a house">
  <h1>Creating Exceptional<br>Outdoor Living Spaces</h1>
  <p>We want to be your outdoor living company!</p>
</section>
<svg class="abs" style="left:0;top:640px" width="1200" height="110" viewBox="0 0 1200 110">
  <path d="M0 30 C300 110 700 110 1200 30 L1200 110 L0 110 Z" fill="var(--white)"/>
  <path d="M0 30 C300 110 700 90 1200 30 L1200 62 C800 105 300 110 0 30 Z" fill="var(--green)"/>
</svg>

<section class="about">
  <div class="abs heading" style="left:161px;top:835px">About Us</div>
  <p class="abs body-copy" style="left:161px;top:883px;width:375px">Brookmoor Greens is a full service landscape construction and maintenance company. We have been servicing the community for over 20 years and in that time have established ourselves as a premier contractor in the Hamptons. We pride ourselves on quality work and excellent customer service.</p>
  <div class="abs photo" style="left:635px;top:810px;width:406px;height:267px;background:linear-gradient(160deg,#5d7a4a,#8fae6a 60%,#4b6b35)" role="img" aria-label="Photo of a gardener mowing a lawn"></div>
</section>

<section class="location">
  <svg class="abs" style="left:0;top:1200px" width="1200" height="335" viewBox="0 0 1200 335">
    <path d="M0 0 H1200 V280 C800 310 400 310 0 300 Z" fill="var(--green)"/>
  </svg>
  <div class="abs" style="left:156px;top:1135px;width:548px;height:299px;background:linear-gradient(135deg,#eef0ee,#e2e6e3)" role="img" aria-label="Street map showing the company location"></div>
  <div class="abs contact-panel" style="left:704px;top:1135px;width:337px;height:299px;padding:52px 38px">
    <h3>Contact Information</h3>
    <p>PO Box 408<br>Alder Bay, NY 10990<br>Phone <b>(555) 014-3371</b><br>Fax (555) 014-3372<br>Mail : hello@brookmoorgreens.example</p>
  </div>
</section>

<section class="services">
  <div class="abs heading" style="left:0;width:1200px;justify-content:center;top:1620px">Our Services</div>

  <div class="abs photo" style="left:161px;top:1723px;width:453px;height:289px;background:linear-gradient(180deg,#6f97c9,#a9c3de 45%,#6e8a55 75%,#5b7a3d)" role="img" aria-label="Photo of a modern house with a curved lawn"></div>
  <div class="abs service" style="left:670px;top:1738px;width:360px">
    <h2>Landscaping</h2>
    <p class="body-copy">Lorem ipsum dolor sit amet, consectetur adipiscing elit. Vulputate sodales ullamcorper pellentesque pulvinar fringilla. Fringilla quam urna sit ut volutpat ultrices nulla. Lectus nisl posuere gravida amet, lacinia mi mi. Congue libero tincidunt nibh massa purus fermentum.</p>
    <span class="btn">Request Estimate</span>
  </div>

  <div class="abs service" style="left:157px;top:2085px;width:360px">
    <h2>Maintenance</h2>
    <p class="body-copy" style="padding-left:4px">Lorem ipsum dolor sit amet, consectetur adipiscing elit. Vulputate sodales ullamcorper pellentesque pulvinar fringilla. Fringilla quam urna sit ut volutpat ultrices nulla. Lectus nisl posuere gravida amet, lacinia mi mi. Congue libero tincidunt nibh massa purus fermentum.</p>
    <span class="btn" style="margin-left:4px">Request Estimate</span>
  </div>
  <div class="abs photo" style="left:588px;top:2080px;width:453px;height:289px;background:linear-gradient(160deg,#3f5a2c,#7d9e4f 55%,#9bb866)" role="img" aria-label="Photo of a gardener servicing a lawn mower on grass"></div>

  <div class="abs photo" style="left:161px;top:2449px;width:453px;height:289px;background:linear-gradient(170deg,#4e6a3a,#8c9a74 45%,#5f7d3c)" role="img" aria-label="Photo of a garden with large rocks, trees and plants"></div>
  <div class="abs service" style="left:670px;top:2464px;width:360px">
    <h2>Flowers</h2>
    <p class="body-copy">Lorem ipsum dolor sit amet, consectetur adipiscing elit. Vulputate sodales ullamcorper pellentesque pulvinar fringilla. Fringilla quam urna sit ut volutpat ultrices nulla. Lectus nisl posuere gravida amet, lacinia mi mi. Congue libero tincidunt nibh massa purus fermentum.</p>
    <span class="btn">Request Estimate</span>
  </div>
</section>

<section class="gallery">
  <div class="abs heading" style="left:0;width:1200px;justify-content:center;top:2845px">Gallery</div>
  <div class="abs photo" style="left:161px;top:2912px;width:278px;height:182px;background:linear-gradient(180deg,#6f97c9,#a9c3de 50%,#6e8a55)" role="img" aria-label="Photo of a modern house with lawn"></div>
  <div class="abs photo" style="left:161px;top:3114px;width:278px;height:349px;background:linear-gradient(180deg,#c9ccc8,#6f7d60 45%,#6b6a3a 75%,#4a5e32)" role="img" aria-label="Photo of a cottage with a brick path and flower beds"></div>
  <div class="abs photo" style="left:463px;top:2912px;width:278px;height:347px;background:linear-gradient(180deg,#3f5a3a,#8a7d6c 55%,#a8a59d)" role="img" aria-label="Photo of a stone pillar, low wall and paved walkway"></div>
  <div class="abs photo" style="left:463px;top:3283px;width:278px;height:180px;background:linear-gradient(180deg,#5f7d45,#a4b58a 35%,#5aa53a 75%,#6cb83f)" role="img" aria-label="Photo of a house front with a colourful flower border"></div>
  <div class="abs photo" style="left:763px;top:2912px;width:278px;height:182px;background:linear-gradient(180deg,#d9dde0,#8d8f8e 55%,#6d9a45)" role="img" aria-label="Photo of a stone patio with outdoor seating behind a house"></div>
  <div class="abs photo" style="left:763px;top:3114px;width:278px;height:349px;background:linear-gradient(180deg,#a89a86,#5a7a3d 50%,#7b4a3c 80%,#4e7a32)" role="img" aria-label="Photo of a house corner with shrubs and flowers"></div>
</section>

<section class="contact-us">
  <svg class="abs" style="left:0;top:3500px" width="1200" height="472" viewBox="0 0 1200 472">
    <path d="M0 45 C400 5 800 5 1200 35 V472 H0 Z" fill="var(--green)"/>
  </svg>
  <div class="abs" style="left:169px;top:3604px;width:380px">
    <h2>Contact Us</h2>
    <p>We look forward to hearing about your project! Provide us with some information below, and we will be sure to get right back to you.</p>
    <p style="margin-top:40px;padding-left:3px">PO Box 408<br>Alder Bay, NY 10990<br>Phone <b>(555) 014-3371</b><br>Fax (555) 014-3372<br>Mail : hello@brookmoorgreens.example</p>
  </div>
  <div class="abs field" style="left:693px;top:3609px;width:348px;height:41px">Name</div>
  <div class="abs field" style="left:693px;top:3662px;width:348px;height:40px">Phone</div>
  <div class="abs field" style="left:693px;top:3715px;width:348px;height:41px">Email</div>
  <div class="abs field" style="left:693px;top:3768px;width:348px;height:108px">How can we help?</div>
  <div class="abs send" style="left:688px;top:3895px;width:63px">SEND</div>
</section>

<footer class="abs footer">
  <div class="social"><span></span><span></span><span></span><span></span><span></span></div>
  <ul><li>Home</li><li>About Us</li><li>Services &#8964;</li><li>Portfolio</li><li>Gallery</li><li>Contact</li></ul>
  <div class="copy">©Copyright 2020 brookmoorgreens</div>
</footer>

</body>
</html>
```